Business card for massage therapy company called Brook Fern Wellness

Need business card for massage therapy company called Brook Fern Wellness. Would like my logo on the front and the back of the card I have 3 options of logos and you can play with what looks better.

Would like this information displayed on the back of the card:

Marcus Ellery
Licensed Massage Therapist
321-555-0147
brookfern-example.com
brookfern_rest_

```html
<!DOCTYPE html>
<html lang="en">
<head>
<meta charset="utf-8">
<title>Brook Fern Wellness – Business Card</title>
<link rel="stylesheet" href="https://fonts.googleapis.com/css2?family=Cinzel:wght@400;500&display=swap">
<style>
  :root {
    --clay: #bf926f;
    --sage: #707862;
    --paper: #ffffff;
  }
  * { margin: 0; padding: 0; box-sizing: border-box; }
  html, body {
    width: 1016px;
    height: 1200px;
    overflow: hidden;
    background: var(--paper);
  }
  .card-sheet {
    position: relative;
    width: 1016px;
    height: 1200px;
    background: var(--paper);
    font-family: "Cinzel", "Times New Roman", serif;
  }
  .front-mark {
    position: absolute;
    left: 32px;
    top: 80px;
    font-size: 38px;
    font-weight: 400;
    color: var(--sage);
    letter-spacing: 1px;
  }
  .therapist-name {
    position: absolute;
    left: 0;
    top: 222px;
    width: 1016px;
    text-align: center;
    font-size: 88px;
    font-weight: 400;
    color: var(--clay);
    letter-spacing: 2px;
    line-height: 1;
  }
  .therapist-title {
    position: absolute;
    left: 0;
    top: 322px;
    width: 1016px;
    text-align: center;
    font-size: 36px;
    font-weight: 400;
    color: var(--clay);
    letter-spacing: 2px;
    line-height: 1;
  }
  .contact-band {
    position: absolute;
    left: 0;
    top: 464px;
    width: 1016px;
    height: 131px;
    background: var(--clay);
    display: flex;
    align-items: center;
    justify-content: center;
    gap: 14px;
    color: var(--paper);
    font-size: 27px;
    letter-spacing: 1px;
  }
  .brand-panel {
    position: absolute;
    left: 0;
    top: 604px;
    width: 1016px;
    height: 596px;
    background: var(--clay);
  }
  .brand-ring {
    position: absolute;
    left: 371px;
    top: 48px;
    width: 276px;
    height: 276px;
  }
  .brand-name {
    position: absolute;
    left: 0;
    width: 1016px;
    text-align: center;
    color: var(--paper);
    font-size: 66px;
    font-weight: 400;
    letter-spacing: 6px;
    line-height: 1;
  }
  .brand-name.line-one { top: 362px; }
  .brand-name.line-two { top: 446px; }
</style>
</head>
<body>
  <main class="card-sheet">
    <section class="card-front-info">
      <div class="front-mark">Brook Fern Wellness</div>
      <h1 class="therapist-name">MARCUS ELLERY</h1>
      <p class="therapist-title">Licensed Massage Therapist</p>
    </section>

    <div class="contact-band">
      <span class="contact-phone">321-555-0147</span>
      <span class="contact-web">brookfern-example.com</span>
      <span class="contact-social">brookfern_rest_</span>
    </div>

    <section class="brand-panel">
      <svg class="brand-ring" viewBox="0 0 276 276" aria-hidden="true">
        <circle cx="138" cy="138" r="135" fill="none" stroke="#ffffff" stroke-width="4"/>
      </svg>
      <div class="brand-name line-one">BROOK FERN</div>
      <div class="brand-name line-two">WELLNESS</div>
    </section>
  </main>
</body>
</html>
```